OutBanished Sentinel and The 9 Doors of Becoming

Create a book cover for Dale Verhoffen first biography and a self-help book about The 9 Doors of Becoming.

US Harbor Lancer uses his battlefield and transition experience to guide you to success in any life challenge.

Back Cover:
Every single human being will go through a life changing event. It could be losing a job of 20 years, a divorce, being an athlete and getting hurt, or retiring from the military. These life changing events can sometime cause disastrous effects on us, our relationships, and some people never recover. This happened to Dale when he left a 12 year carrier as a Harbor Lancer with Coastal Vanguard Command. He then took the skills he learned as a Lancer and got to work solving the problem.

The OutBanished Sentinel takes us through a journey of Dale’s Transition out of Vanguard Command as he attempts to reintegrate in to civilian life. Through this Journey he found 7 different stages of transition and this book outlines them and what you can do about.

Target Market(s)

Military, Veterans

Industry/Entity Type

Military

Other font styles liked:
• Bebas Neu

Colors

Designer to choose colors to be used in the design.

Requirements
Must have
• Must have the cover image title, and my name.
• US Harbor Lancer uses his battlefield and transition experience to guide you to success in any life challenge.
Nice to have
• Would be nice to fit the device in the design somewhere maybe next to my name if it fits well.
• Back Cover:
• Every single human being will go through a life changing event. It could be losing a job of 20 years, a divorce, being an athlete and getting hurt, or retiring from the military. These life changing events can sometime cause disastrous effects on us, our relationships, and some people never recover. This happened to Dale when he left a 12 year carrier as a Harbor Lancer with Coastal Vanguard Command. He then took the skills he learned as a Lancer and got to work solving the problem.
• The OutBanished Sentinel takes us through a journey of Dale’s Transition out of Vanguard Command as he attempts to reintegrate in to civilian life. Through this Journey he found 7 different stages of transition and this book outlines them and what you can do about.
Should not have
• No Coastal Heron wheel and trident.

```html
<!DOCTYPE html>
<html lang="en">
<head>
<meta charset="utf-8">
<title>Dale Verhoffen — The 9 Doors of Becoming</title>
<link rel="stylesheet" href="https://fonts.googleapis.com/css2?family=Bebas+Neue&display=swap">
<style>
  :root {
    --band: #561713;
    --title: #ffffff;
    --tagline: #f3d9cc;
    --scene-light: #f6d7ea;
    --scene-mid: #e79ab8;
    --scene-warm: #e0704c;
    --portrait-light: #f3dccb;
    --portrait-mid: #8a4a2c;
    --portrait-dark: #2b140c;
  }
  html, body {
    margin: 0;
    padding: 0;
    overflow: hidden;
    background: #ffffff;
  }
  .cover {
    position: relative;
    width: 800px;
    height: 1200px;
    overflow: hidden;
    font-family: "Bebas Neue", "Oswald", sans-serif;
  }
  .band {
    position: absolute;
    left: 0;
    width: 800px;
    background: var(--band);
    color: var(--title);
    line-height: 1;
    white-space: nowrap;
    text-align: center;
  }
  .band--author {
    top: 0;
    height: 250px;
  }
  .author-name {
    position: absolute;
    left: 0;
    right: 0;
    top: 78px;
    margin: 0;
    font-weight: 400;
    font-size: 110px;
    letter-spacing: 1px;
  }
  .tagline {
    position: absolute;
    left: 40px;
    right: 40px;
    top: 196px;
    margin: 0;
    font-size: 20px;
    line-height: 22px;
    letter-spacing: 1.5px;
    white-space: normal;
    color: var(--tagline);
  }
  .band--title {
    bottom: 0;
    height: 182px;
    display: flex;
    align-items: center;
    justify-content: center;
  }
  .book-title {
    margin: 0;
    font-weight: 400;
    font-size: 104px;
    letter-spacing: 1px;
  }
  .scene {
    position: absolute;
    top: 250px;
    left: 0;
    width: 800px;
    height: 768px;
    display: block;
  }
</style>
</head>
<body>
  <main class="cover">
    <header class="band band--author">
      <p class="author-name">Dale Verhoffen</p>
      <p class="tagline">US Harbor Lancer uses his battlefield and transition experience<br>to guide you to success in any life challenge.</p>
    </header>

    <svg class="scene" viewBox="0 250 800 768" xmlns="http://www.w3.org/2000/svg">
      <defs>
        <linearGradient id="forest-tone" x1="0" y1="0" x2="1" y2="1">
          <stop offset="0" stop-color="var(--scene-mid)"/>
          <stop offset="0.45" stop-color="var(--scene-light)"/>
          <stop offset="1" stop-color="var(--scene-warm)"/>
        </linearGradient>
        <linearGradient id="portrait-tone" x1="0" y1="0" x2="0.4" y2="1">
          <stop offset="0" stop-color="var(--portrait-light)"/>
          <stop offset="0.35" stop-color="var(--portrait-mid)"/>
          <stop offset="1" stop-color="var(--portrait-dark)"/>
        </linearGradient>
      </defs>

      <rect class="scene__landscape" x="0" y="250" width="800" height="768"
            fill="url(#forest-tone)" role="img"
            aria-label="Snowy mountain valley with pine forest in pink and orange tones"/>

      <path class="scene__numeral" fill-rule="evenodd" fill="url(#portrait-tone)"
            role="img" aria-label="Portrait of the author in tactical gear framed inside a large numeral nine"
            d="M85 282 L715 290 L535 1018 L228 1018 L318 740 L85 740 Z
               M225 400 L572 404 L520 615 L225 615 Z"/>
    </svg>

    <footer class="band band--title">
      <h1 class="book-title">Doors of Becoming</h1>
    </footer>
  </main>
</body>
</html>
```